Business Card Design for Telecommunications and IT Solutions company "OKRA"

BC for telecommunications company name "OKRA" with slogan "Telecom & IT Solutions"

should have the full name as above "OKRA" and the slogan
color reqiured black, red (dark) and white

simple, professional, serious, modern design is required

1 side of business card have a full details, contacts and logo
other side have only the logo, website and full company name "ALOKRA Company for Telecommunications service & Information Technology LLC"

i have attached the logo and current business card sample and note that the logo was changed not the same in the attached business card

Industry/Entity Type

Telecommunications

Contact Information for Business Card

Full name: Omar Nabil Al Hudari
Job title: General Manager
Mobile no: +964xxxxxxxxx
email: omar@okra-tel.example
full name of the company: ALOKRA Company Telecommunications Services & Information Technology LLC.
website: www.okra-tel.example
address: Nakheel Dist. 148/7 JubailaQadim, Basra, Iraq

Requirements
Must have
• two languages in the same side of business card (English, Arabic) for only the name and title

```html
<!DOCTYPE html>
<html lang="en">
<head>
<meta charset="utf-8">
<title>OKRA Telecom &amp; IT Solutions – Business Card</title>
<link href="https://fonts.googleapis.com/css2?family=Open+Sans:wght@400;600;700&family=Cairo:wght@400;600;700&display=swap" rel="stylesheet">
<style>
  :root {
    --brand-red: #a8141b;
    --brand-red-dark: #8e0f15;
    --ink: #1b1b1b;
    --ink-soft: #6d6d6d;
    --paper: #ffffff;
    --stage: #ecebe8;
    --rule: #b9b9b9;
  }
  * { box-sizing: border-box; margin: 0; padding: 0; }
  html, body { width: 1200px; height: 1000px; overflow: hidden; }
  body {
    background: var(--stage);
    font-family: "Open Sans", Arial, sans-serif;
    position: relative;
  }
  .card {
    position: absolute;
    width: 540px;
    height: 310px;
    border-radius: 3px;
    overflow: hidden;
    box-shadow: 0 10px 28px rgba(0,0,0,0.18);
  }
  .arabic { font-family: "Cairo", "Noto Sans Arabic", sans-serif; direction: rtl; }

  /* Front: red side */
  .card--front { left: 50px; top: 150px; background: var(--brand-red); color: var(--paper); }
  .front__brand {
    position: absolute; left: 0; right: 0; top: 70px;
    display: flex; flex-direction: column; align-items: center;
  }
  .wordmark { font-weight: 600; letter-spacing: 6px; line-height: 1; }
  .card--front .wordmark { font-size: 74px; color: var(--paper); }
  .slogan { font-weight: 400; letter-spacing: 1.5px; text-transform: uppercase; }
  .card--front .slogan { font-size: 17px; margin-top: 8px; }
  .card--front .company-ar { font-size: 17px; font-weight: 600; margin-top: 4px; line-height: 1.3; }
  .card--front .company-ar-full { font-size: 15px; font-weight: 600; line-height: 1.3; }

  /* Back: details side */
  .card--back { left: 610px; top: 480px; background: var(--paper); color: var(--ink); }
  .back__swoosh { position: absolute; inset: 0; width: 100%; height: 100%; }
  .back__brand {
    position: absolute; right: 40px; top: 34px;
    display: flex; flex-direction: column; align-items: flex-end;
  }
  .card--back .wordmark { font-size: 58px; color: var(--ink); }
  .card--back .slogan { font-size: 14px; margin-top: 4px; }
  .card--back .company-ar { font-size: 16px; font-weight: 700; color: var(--brand-red); line-height: 1.3; margin-top: 2px; }
  .card--back .company-ar-full { font-size: 13px; font-weight: 600; line-height: 1.3; }

  .person {
    position: absolute; left: 18px; top: 166px; width: 166px;
    text-align: right; white-space: nowrap;
  }
  .person__name { font-size: 13.5px; font-weight: 700; color: var(--brand-red); line-height: 1.45; }
  .person__title { font-size: 12px; color: var(--ink-soft); line-height: 1.4; }
  .person__name-ar { font-size: 16px; font-weight: 600; color: var(--brand-red); line-height: 1.3; }
  .person__title-ar { font-size: 13px; color: var(--ink-soft); line-height: 1.2; }

  .divider { position: absolute; left: 194px; top: 168px; width: 1px; height: 90px; background: var(--rule); }

  .contact {
    position: absolute; left: 206px; top: 166px;
    font-size: 11.5px; font-weight: 600; line-height: 1.55;
    white-space: nowrap;
  }
  .contact__row { display: flex; align-items: center; gap: 6px; }
  .contact__row + .contact__row { margin-top: 3px; }
  .icon { width: 12px; height: 12px; flex: none; fill: var(--brand-red); }
  .contact__address { margin-bottom: 3px; }
  .contact__pair { display: flex; gap: 14px; }
</style>
</head>
<body>

  <section class="card card--front" aria-label="Business card front">
    <div class="front__brand">
      <div class="wordmark">OKRA</div>
      <div class="slogan">Telecom &amp; IT Solutions</div>
      <div class="company-ar arabic">شركة أوكرا</div>
      <div class="company-ar-full arabic">خدمات الإتصالات وتقنية المعلومات المحدودة</div>
    </div>
  </section>

  <section class="card card--back" aria-label="Business card back">
    <svg class="back__swoosh" viewBox="0 0 540 310" preserveAspectRatio="none" aria-hidden="true">
      <path d="M0 0 H540 V0 C420 0 300 20 180 38 C110 48 50 40 0 28 Z" fill="#e4e4e4"/>
      <path d="M540 268 C505 290 450 304 400 310 H540 Z" fill="var(--brand-red)"/>
      <path d="M540 252 C500 282 440 302 370 310 H400 C450 304 505 290 540 268 Z" fill="var(--brand-red-dark)" opacity="0.35"/>
    </svg>

    <div class="back__brand">
      <div class="wordmark">OKRA</div>
      <div class="slogan">Telecom &amp; IT Solutions</div>
      <div class="company-ar arabic">شركة أوكرا</div>
      <div class="company-ar-full arabic">خدمات الإتصالات وتقنية المعلومات المحدودة</div>
    </div>

    <div class="person">
      <div class="person__name">Omar Nabil Al Hudari</div>
      <div class="person__title">General Manager</div>
      <div class="person__name-ar arabic">عمر نبيل الحضري</div>
      <div class="person__title-ar arabic">المدير العام</div>
    </div>

    <div class="divider"></div>

    <div class="contact">
      <div class="contact__address">Nakheel Dist. 148/7 JubailaQadim<br>Basra, Iraq</div>
      <div class="contact__row">
        <svg class="icon" viewBox="0 0 12 16" aria-label="Mobile"><path d="M2 0h8a2 2 0 0 1 2 2v12a2 2 0 0 1-2 2H2a2 2 0 0 1-2-2V2a2 2 0 0 1 2-2zm0 2v10h8V2zm4 11a1 1 0 1 0 0 2 1 1 0 0 0 0-2z"/></svg>
        <span>964 77000 555 01, 964 78000 555 02</span>
      </div>
      <div class="contact__row contact__pair">
        <span class="contact__row">
          <svg class="icon" viewBox="0 0 16 12" aria-label="Email"><path d="M0 0h16v12H0zm1.5 1.2L8 6.4l6.5-5.2z"/></svg>
          <span>omar@okra-tel.example</span>
        </span>
        <span class="contact__row">
          <svg class="icon" viewBox="0 0 16 16" aria-label="Website"><path d="M8 0a8 8 0 1 0 0 16A8 8 0 0 0 8 0zm-1 1.6V5H4.3A6.5 6.5 0 0 1 7 1.6zm2 0A6.5 6.5 0 0 1 11.7 5H9zM3.7 6.5H7v3H3.7a6.7 6.7 0 0 1 0-3zm5.3 0h3.3a6.7 6.7 0 0 1 0 3H9zM4.3 11H7v3.4A6.5 6.5 0 0 1 4.3 11zM9 11h2.7A6.5 6.5 0 0 1 9 14.4z"/></svg>
          <span>www.okra-tel.example</span>
        </span>
      </div>
    </div>
  </section>

</body>
</html>
```